Werbebrief
Zielgruppe
Unsere Zielgruppe sind Geschäftsführer junger Unternehmen.
Hallo,
Wir benötigen einen "Werbebrief". Es ist jedoch weniger ein Brief, als viel mehr eine etwas größerer "Werbekarte" (diese soll 105 x 210mm groß sein).
Auf der Vorderseite soll folgender Text stehen:
Für Unternehmen, die gerne expandieren möchten
Auf der Rückseite soll folgender Link stehen:
www.tessaro-werk.de/Expandieren
Darunter soll folgendes stehen:
Ihr persönlicher Code: ABC123
Wichtig ist, dass wir den Code individuell ändern können, da jeder einen anderen Code bekommt.
Unser Logo und Corporate Farbe habe ich hochgeladen. Das Design sollte auf jeden Fall zu unserer Webseite passen (www.tessaro-werk.de)
Wir freuen uns auf Ihre Vorschläge.

```html
<!DOCTYPE html>
<html lang="de">
<head>
<meta charset="utf-8">
<title>Tessaro Werk – Werbekarte</title>
<link rel="stylesheet" href="https://fonts.googleapis.com/css2?family=Arimo:ital,wght@0,400;0,700;1,700&display=swap">
<style>
  :root {
    --card-blue: #0e4a84;
    --card-text: #ffffff;
    --page-bg: #f2f2f0;
    --card-shadow: rgba(0, 0, 0, 0.35);
  }
  * { box-sizing: border-box; margin: 0; padding: 0; }
  html, body {
    width: 1200px;
    height: 796px;
    overflow: hidden;
  }
  body {
    background: var(--page-bg);
    font-family: "Arimo", Arial, sans-serif;
    color: var(--card-text);
    position: relative;
  }
  .card {
    position: absolute;
    width: 600px;
    height: 300px;
    background: var(--card-blue);
    box-shadow: 4px 6px 10px var(--card-shadow);
  }
  .card--front { left: 110px; top: 90px; }
  .card--back { left: 490px; top: 410px; }

  .brand {
    position: absolute;
    left: 90px;
    top: 118px;
  }
  .brand__line {
    display: flex;
    align-items: center;
    gap: 10px;
  }
  .brand__dot {
    width: 22px;
    height: 22px;
    border-radius: 50%;
    background: var(--card-text);
  }
  .brand__name {
    font-size: 26px;
    font-weight: 400;
    letter-spacing: 0.2px;
  }
  .brand__tagline {
    margin-top: 6px;
    margin-left: 32px;
    font-size: 10px;
  }

  .back__content {
    position: absolute;
    inset: 0;
    display: flex;
    flex-direction: column;
    align-items: center;
    justify-content: center;
    gap: 16px;
    padding-bottom: 30px;
  }
  .back__link {
    font-size: 16px;
    font-weight: 700;
    font-style: italic;
  }
  .back__code {
    font-size: 16px;
    font-weight: 400;
  }
</style>
</head>
<body>
  <section class="card card--front" aria-label="Vorderseite">
    <div class="brand">
      <div class="brand__line">
        <span class="brand__dot" aria-hidden="true"></span>
        <span class="brand__name">Tessaro Werk</span>
      </div>
      <p class="brand__tagline">Für Unternehmen, die gerne expandieren möchten</p>
    </div>
  </section>

  <section class="card card--back" aria-label="Rückseite">
    <div class="back__content">
      <p class="back__link">http://www.tessaro-werk.de/expandieren</p>
      <p class="back__code">Ihr persönlicher Code: ABC123</p>
    </div>
  </section>
</body>
</html>
```